Website design for management consulting firm

We need a web design for a new consulting company based in Boston, MA called "Fernhollow Ridge Consulting." This webpage will be simple home page, with a "contact us" page, that describes the services of the consulting firm. The company provides strategic planning, business assessment, process re-designs, and other management consulting functions. I would like the website to look high-tech. A logo was already created via Pixel Harbor.

Target Market(s)

Other business owners across a wide spectrum of industries - from IT to retail.

Industry/Entity Type

It Company

Number of Pages Required

3 page

Colors
0455a3
ffffff

Requirements
Must have
• Front page that provides generic text / overview of the firm. A "services" tab that describes consulting services. A "contact us" tab that provides either a form to contact us or just the contact email address of the company. info@fernhollowridgeconsulting.example

```html
<!DOCTYPE html>
<html lang="en">
<head>
<meta charset="utf-8">
<title>Fernhollow Ridge Consulting</title>
<link rel="stylesheet" href="https://fonts.googleapis.com/css2?family=Open+Sans:wght@400;600;700&display=swap">
<style>
:root{
  --brand:#0455a3;
  --brand-dark:#0a4f8f;
  --white:#ffffff;
  --ink:#333333;
  --muted:#555555;
  --teal:#3fc8c0;
  --band:#f1f1f1;
  --footer:#231f20;
  --hero-a:#2a2a2a;
  --hero-b:#5a5a5a;
}
*{margin:0;padding:0;box-sizing:border-box}
html,body{width:1179px;height:1200px;overflow:hidden;background:var(--white)}
body{font-family:"Open Sans",Arial,sans-serif;color:var(--ink);position:relative}
.site-header{position:absolute;left:0;top:0;width:1179px;height:80px;background:var(--white)}
.brand{position:absolute;left:134px;top:16px;display:flex;align-items:center;gap:10px}
.brand-mark{width:46px;height:46px;background:var(--brand)}
.brand-name{font-size:22px;font-weight:700;color:#1b1b1b;line-height:1.05;width:200px}
.main-nav{position:absolute;left:795px;top:27px;display:flex;align-items:center;gap:0}
.main-nav a{font-size:13px;color:#333;text-decoration:none;padding:0 18px;line-height:29px}
.main-nav a.is-active{background:var(--brand);color:var(--white);border-radius:3px;width:71px;text-align:center;padding:0;margin-right:10px}
.hero{position:absolute;left:0;top:80px;width:1179px;height:354px;background:linear-gradient(90deg,var(--hero-a),var(--hero-b) 55%,#3a3a3a)}
.hero-title{position:absolute;left:150px;top:78px;font-size:28px;font-weight:400;color:var(--teal)}
.hero-points{position:absolute;left:153px;top:135px;list-style:none}
.hero-points li{display:flex;align-items:flex-start;gap:14px;height:48px;color:var(--white);font-size:14px;line-height:17px}
.hero-points svg{flex:none;margin-top:6px}
.hero-portrait{position:absolute;left:692px;top:8px;width:276px;height:346px;background:linear-gradient(180deg,#4d4d4d,#1c2a45 60%,#16223a)}
.about{position:absolute;left:136px;top:456px;width:910px}
.section-title{font-size:22px;font-weight:600;color:var(--brand-dark);letter-spacing:.5px}
.about p{margin-top:12px;font-size:12px;line-height:19.5px;color:var(--muted)}
.services{position:absolute;left:0;top:620px;width:1179px;height:270px;background:var(--band)}
.service{position:absolute;top:32px;width:210px;margin-left:-105px;text-align:center}
.service h3{font-size:18px;font-weight:600;color:#2b2b2b}
.service svg{display:block;margin:20px auto 0}
.service p{margin-top:18px;font-size:11.5px;line-height:18px;color:#444}
.testimonials{position:absolute;left:0;top:916px;width:1179px;text-align:center}
.testimonials blockquote{width:580px;margin:14px auto 0;font-size:12.5px;line-height:19px;color:#444}
.client-avatar{width:60px;height:60px;border-radius:50%;margin:26px auto 0;background:linear-gradient(180deg,#c9b9a8,#7d6a5c)}
.client-name{margin-top:14px;font-size:12px;color:#444}
.site-footer{position:absolute;left:0;top:1166px;width:1179px;height:34px;background:var(--footer);color:var(--white);font-size:11px}
.copyright{position:absolute;left:134px;top:10px}
.footer-nav{position:absolute;right:149px;top:10px}
.footer-nav a{color:var(--white);text-decoration:none}
.footer-nav span{margin:0 9px}
</style>
</head>
<body>
<header class="site-header">
  <div class="brand"><div class="brand-mark"></div><div class="brand-name">Fernhollow Ridge Consulting</div></div>
  <nav class="main-nav"><a class="is-active" href="#">Home</a><a href="#">Services</a><a href="#">Contact Us</a></nav>
</header>

<section class="hero">
  <h1 class="hero-title">Get The Best Solution For Your Business.</h1>
  <ul class="hero-points">
    <li><svg width="22" height="22" viewBox="0 0 22 22"><circle cx="11" cy="11" r="10" fill="#fff"/><path d="M6 11.5l3.3 3.3L16 8" fill="none" stroke="#0455a3" stroke-width="2.4"/></svg><span>Lorem Ipsum is simply dummy text of the printing<br>and typesetting industry.</span></li>
    <li><svg width="22" height="22" viewBox="0 0 22 22"><circle cx="11" cy="11" r="10" fill="#fff"/><path d="M6 11.5l3.3 3.3L16 8" fill="none" stroke="#0455a3" stroke-width="2.4"/></svg><span>Lorem Ipsum is simply dummy text of the printing<br>and typesetting industry.</span></li>
    <li><svg width="22" height="22" viewBox="0 0 22 22"><circle cx="11" cy="11" r="10" fill="#fff"/><path d="M6 11.5l3.3 3.3L16 8" fill="none" stroke="#0455a3" stroke-width="2.4"/></svg><span>Lorem Ipsum is simply dummy text of the printing<br>and typesetting industry.</span></li>
  </ul>
  <div class="hero-portrait" role="img" aria-label="Photo of a smiling businessman in a dark suit with arms crossed"></div>
</section>

<section class="about">
  <h2 class="section-title">About Us</h2>
  <p>Lorem Ipsum is simply dummy text of the printing and typesetting industry. Lorem Ipsum has been the industry's standard dummy text ever since the 1500s, when an unknown printer took a galley of type and scrambled it to make a type specimen book. It has survived not only five centuries, but also the leap into electronic typesetting, remaining essentially unchanged. It was popularised in the 1960s with the release of Letraset sheets containing Lorem Ipsum passages, and more recently with desktop publishing software like Aldus PageMaker including versions of Lorem Ipsum.</p>
</section>

<section class="services">
  <article class="service" style="left:239px">
    <h3>Strategic Planning</h3>
    <svg width="90" height="82" viewBox="0 0 90 82"><path d="M2 2h26a9 9 0 1 1 14 0h18v20a9 9 0 1 0 0 14v16H42a9 9 0 1 0-14 0H2z" fill="#0455a3"/><path d="M50 46l12-12 10 10a8 8 0 1 1 10 10l8 8-18 18-8-8a8 8 0 1 0-10-10z" fill="#0455a3"/></svg>
    <p>Lorem Ipsum is simply dummy text of<br>the printing and typesetting industry.<br>Lorem Ipsum has been</p>
  </article>
  <article class="service" style="left:472px">
    <h3>Business Assessment</h3>
    <svg width="90" height="82" viewBox="0 0 90 82"><path d="M32 14V8h26v6h-5v-3H37v3z" fill="#0455a3"/><rect x="6" y="16" width="78" height="58" rx="4" fill="#0455a3"/><path d="M6 40h78" stroke="#f1f1f1" stroke-width="3"/><rect x="37" y="34" width="16" height="12" rx="2" fill="#f1f1f1"/></svg>
    <p>Lorem Ipsum is simply dummy text of<br>the printing and typesetting industry.<br>Lorem Ipsum has been</p>
  </article>
  <article class="service" style="left:706px">
    <h3>Process Re-designs</h3>
    <svg width="90" height="82" viewBox="0 0 90 82"><path d="M44 4c18 0 30 12 30 28 0 7-3 12-6 16v30H40V68h-8c-5 0-8-3-8-8v-8l-8-4 8-12C24 18 30 4 44 4z" fill="#0455a3"/><circle cx="48" cy="32" r="12" fill="none" stroke="#f1f1f1" stroke-width="5" stroke-dasharray="5 3"/><circle cx="48" cy="32" r="4" fill="#f1f1f1"/></svg>
    <p>Lorem Ipsum is simply dummy text of<br>the printing and typesetting industry.<br>Lorem Ipsum has been</p>
  </article>
  <article class="service" style="left:940px">
    <h3>Other Management</h3>
    <svg width="90" height="82" viewBox="0 0 90 82"><circle cx="42" cy="40" r="26" fill="none" stroke="#0455a3" stroke-width="12" stroke-dasharray="10 6.3"/><circle cx="42" cy="40" r="22" fill="#0455a3"/><circle cx="40" cy="38" r="10" fill="none" stroke="#f1f1f1" stroke-width="4"/><path d="M47 45l18 18" stroke="#f1f1f1" stroke-width="9"/><path d="M48 46l16 16" stroke="#0455a3" stroke-width="5"/></svg>
    <p>Lorem Ipsum is simply dummy text of<br>the printing and typesetting industry.<br>Lorem Ipsum has been</p>
  </article>
</section>

<section class="testimonials">
  <h2 class="section-title">What our client say</h2>
  <blockquote>"Lorem Ipsum is simply dummy text of the printing and typesetting industry. Lorem Ipsum has been the industry's standard dummy text ever since the 1500s, when an unknown printer took a galley of type and scrambled it to make a type specimen book."</blockquote>
  <div class="client-avatar" role="img" aria-label="Portrait photo of the client"></div>
  <p class="client-name">Dara Quill, LEDGER WEEKLY</p>
</section>

<footer class="site-footer">
  <p class="copyright">© Copyright 2015. Fernhollowridgeconsulting.example. All Rights Reserved</p>
  <nav class="footer-nav"><a href="#">Home</a><span>|</span><a href="#">Services</a><span>|</span><a href="#">Contact Us</a></nav>
</footer>
</body>
</html>
```